Carpal Tunnel - PPC Landing Page

We need to do a SINGLE page landing page for a doctor who specializes in Carpal Tunnel syndrome - please research if you're not familiar - it's very common.

Landing page essentials:
Must have a form in upper right hand corner:
Form title: "Get a free diagnosis."
Form inputs: Name, Phone, Email, Requested Appointment time

Page is for PPC, so needs to be simple and light on content. Content has been provided and attached to this project.

No navigation, just a single page.

Industry/Entity Type

Health

Coding

Coded - Design and coding required

Number of Pages Required

1 page

Requirements
Must have
• Elegant look - Conversion optimized for form and phone
• Responsive design.
Should not have
• Old outdated images.

```html
<!DOCTYPE html>
<html lang="en">
<head>
<meta charset="utf-8">
<title>Dr. Halvern's Clinical Practice – Carpal Tunnel Syndrome</title>
<link rel="stylesheet" href="https://fonts.googleapis.com/css2?family=Open+Sans:ital,wght@0,400;0,600;0,700;0,800;1,400;1,700;1,800&display=swap">
<style>
:root{
  --navy:#0c3a8e;
  --navy-dark:#082c70;
  --blue:#1c5fbf;
  --button:#2d7be0;
  --text:#555b66;
  --muted:#7a808a;
  --line:#d7dce4;
  --panel:#f3f5f9;
  --white:#ffffff;
}
*{box-sizing:border-box;margin:0;padding:0}
html,body{width:779px;height:1200px;overflow:hidden}
body{font-family:"Open Sans",Arial,sans-serif;color:var(--text);background:var(--white);position:relative}
.bar{background:var(--navy);height:72px;display:flex;align-items:center;justify-content:space-between;padding:0 28px 0 32px}
.brand{color:var(--white);font-weight:800;font-style:italic;font-size:17px}
.contact{display:flex;align-items:center;gap:8px;color:var(--white)}
.contact svg{width:24px;height:24px}
.contact small{display:block;font-size:7px;letter-spacing:.5px;font-weight:600}
.contact strong{display:block;font-size:15px;font-weight:800;line-height:1.1}
.hero{display:flex;height:300px;padding:14px 32px 0 48px;gap:22px}
.hero-photo{width:310px;height:272px;background:radial-gradient(circle at 60% 40%,#f3e4da 0%,#e9d1c2 40%,#f7f3f0 75%,#fff 100%)}
.hero-copy{flex:1;padding-top:8px}
.hero-copy h1{color:var(--navy);font-size:14px;font-weight:700;margin-bottom:10px}
.hero-copy p{font-size:8px;line-height:1.5;margin-bottom:9px}
.main{display:flex;padding:10px 24px 0 64px;gap:12px}
.conditions{width:470px}
.conditions-label{background:var(--panel);border:1px solid var(--line);font-size:7.5px;font-weight:700;color:#333;padding:7px 8px;margin-bottom:12px}
.condition{margin-bottom:12px}
.condition h2{color:var(--blue);font-size:11px;font-weight:700;margin-bottom:4px}
.condition p{font-size:7.6px;line-height:1.5}
.sidebar{width:210px}
.form{background:var(--navy);padding:12px 14px 18px;color:var(--white)}
.form h3{font-size:12px;font-weight:800;text-align:center;margin-bottom:10px}
.form label{display:block;font-size:7.5px;margin:6px 0 3px}
.form .field{height:22px;background:var(--white);border:1px solid var(--line)}
.form .submit{margin-top:12px;height:30px;background:var(--button);border:1px solid #7fb0f0;color:var(--white);font-weight:800;font-size:13px;display:flex;align-items:center;justify-content:center;letter-spacing:.5px}
.quote{margin:22px 4px 0;font-size:7.5px;font-style:italic;line-height:1.5;color:var(--text)}
.quote cite{display:block;text-align:right;font-weight:700;font-style:normal;color:#333;margin-top:3px}
.foot{position:absolute;left:0;right:0;bottom:0;height:72px;background:var(--navy);display:flex;align-items:center;justify-content:space-between;padding:0 28px 0 32px}
.foot .brand{font-size:15px}
.foot address{color:#c9d6ee;font-size:6.5px;font-style:normal;margin-top:3px}
</style>
</head>
<body>
<header class="bar">
  <div class="brand">Dr. Halvern's Clinical Practice</div>
  <div class="contact">
    <svg viewBox="0 0 24 24"><circle cx="12" cy="12" r="11" fill="none" stroke="#fff" stroke-width="1.5"/><path d="M8.5 6.5l2 2.2-1.2 1.5c.8 1.7 2 2.9 3.5 3.6l1.5-1.2 2.2 2-1.2 1.9c-3.6-.4-7.4-4.2-7.8-7.8z" fill="#fff"/></svg>
    <div><small>CONTACT US NOW</small><strong>08-555-014-2270</strong></div>
  </div>
</header>

<section class="hero">
  <div class="hero-photo" role="img" aria-label="Photo of a woman holding her sore wrist"></div>
  <div class="hero-copy">
    <h1>What is Carpal Tunnel Syndrome</h1>
    <p>In Dr. Halvern's clinical practice, Carpal Tunnel Syndrome is one of the most commonly treated health problems. Carpal tunnel occurs when swelling pinches the median nerve, which provides sensation to the palm side of the thumb, index finger, middle finger and part of the ring finger.</p>
    <p>This build-up can be a combination of tingling, numbness, weakness and pain in the fingers, thumb, palm or the forearm. If the condition is not treated, permanent deterioration of muscle tissue can occur.</p>
  </div>
</section>

<main class="main">
  <div class="conditions">
    <div class="conditions-label">Other Conditions Treated by Dr. Halvern</div>
    <article class="condition">
      <h2>Cubital Tunnel Syndrome (Cell Phone Elbow)</h2>
      <p>Similar to carpal tunnel syndrome, cubital tunnel syndrome is a condition brought on by increased pressure. This occurs when there is increased pressure on the ulnar nerve at the elbow. The nerve travels on the inner portion of the elbow, commonly known as the funny bone. It is used when the arm is bent. As this position puts the ulnar nerve in constant stretch, blood flow to the nerve is reduced and numbness sets in. Symptoms include pins and needles in the ring and little fingers, weakened grip and aching pain along the forearm.</p>
    </article>
    <article class="condition">
      <h2>DeQuervains Tenosynovitis</h2>
      <p>Also known as first dorsal compartment tenosynovitis, this is one of the most common hand problems seen by Dr. Halvern. It is a condition where the tendons on the thumb side of the wrist become irritated and swollen. Repetitive gripping, lifting a baby, or twisting the wrist can all bring on symptoms. The condition causes pain when turning the wrist, making a fist or grasping objects, and usually responds well to splinting, rest and guided treatment.</p>
    </article>
    <article class="condition">
      <h2>Dupuytren's Disease</h2>
      <p>Dupuytren's Disease is caused by an abnormal thickening in the palm and fingers. This limits hand movement. Although the exact cause of Dupuytren's is not known, heredity plays a significant role. It commonly affects people over the age of fifty and is more frequent in men. Firm lumps and cords form under the skin and slowly pull the fingers into a bent position. Early assessment allows Dr. Halvern to monitor progress and recommend the right treatment before movement is lost.</p>
    </article>
    <article class="condition">
      <h2>Hand Fractures</h2>
      <p>Fractures of the finger occur when the finger or hand is hit by a solid object with force. Fractures are most common at the base of the little finger, often called a boxer's fracture. Minor injuries may be treated with a splint, while displaced breaks need careful alignment. Prompt assessment of swelling, deformity or loss of movement helps the bone heal in the correct position and avoids long-term stiffness.</p>
    </article>
    <article class="condition">
      <h2>Hand Fractures</h2>
      <p>Fractures of the hand should be treated promptly to avoid lasting problems with grip and strength. Many of these injuries occur during sport, falls or workplace accidents. Dr. Halvern offers thorough examination, imaging and a clear plan for casting, therapy or surgery so patients can return to daily activities with confidence.</p>
    </article>
    <article class="condition">
      <h2>Hand Fractures</h2>
      <p>Sprains result from forcing a joint to perform a function against its normal range of motion. Finger sprains occur when the ligaments that support the joint are stretched or torn. Common examples are jammed fingers from ball sports. If symptoms persist for more than a few days, a professional assessment is recommended.</p>
    </article>
  </div>

  <aside class="sidebar">
    <div class="form">
      <h3>GET A FREE DIAGNOSIS</h3>
      <label>Name</label><div class="field"></div>
      <label>Phone</label><div class="field"></div>
      <label>Email</label><div class="field"></div>
      <label>Requested Appointment Time</label><div class="field"></div>
      <div class="submit">SUBMIT</div>
    </div>
    <blockquote class="quote">" I carried my treatment appointments 6 weeks before my event. Along with the treatment and the excellent advice I was given I began to feel a huge improvement."<cite>Martin K.</cite></blockquote>
    <blockquote class="quote">"Very pleased with treatment and advice. Good value and gave lots of advice to help prevent this problem coming back again."<cite>Paul Reyes</cite></blockquote>
  </aside>
</main>

<footer class="foot">
  <div>
    <div class="brand">Dr. Halvern's Clinical Practice</div>
    <address>12 Lindell Avenue, Westbury VIC, Australia 3187</address>
  </div>
  <div class="contact">
    <svg viewBox="0 0 24 24"><circle cx="12" cy="12" r="11" fill="none" stroke="#fff" stroke-width="1.5"/><path d="M8.5 6.5l2 2.2-1.2 1.5c.8 1.7 2 2.9 3.5 3.6l1.5-1.2 2.2 2-1.2 1.9c-3.6-.4-7.4-4.2-7.8-7.8z" fill="#fff"/></svg>
    <div><small>CONTACT US NOW</small><strong>08-555-014-2270</strong></div>
  </div>
</footer>
</body>
</html>
```